Wine Label Marabel Faye Rose or Pinot Noir

Need label design for "Marabel Faye" wine brand.
Rose or Pinot Noir.
Thinking something pretty, floral, southern inspired.

Target Market(s)

Female- age 45-65

Font styles to use
Script

Colors
eea4c8
d2a4cc
f68e4d
fee18a

```html
<!DOCTYPE html>
<html lang="en">
<head>
<meta charset="utf-8">
<title>Marabel Faye Pinot Noir Label</title>
<link rel="stylesheet" href="https://fonts.googleapis.com/css2?family=Allura&family=Montserrat:wght@400&display=swap">
<style>
  :root {
    --canvas-bg: #e9e7e6;
    --label-paper: #f7f2ef;
    --ink: #2a2624;
    --petal-light: #f5d9cb;
    --petal-mid: #e9b39c;
    --petal-deep: #d98e78;
    --flower-core: #8e2a1e;
    --splash: #efc9c4;
  }
  * { margin: 0; padding: 0; box-sizing: border-box; }
  html, body {
    width: 801px;
    height: 1200px;
    overflow: hidden;
    background: var(--canvas-bg);
  }
  .canvas {
    position: relative;
    width: 801px;
    height: 1200px;
  }
  .wine-label {
    position: absolute;
    left: 20px;
    top: 80px;
    width: 760px;
    height: 1040px;
    background: var(--label-paper);
    overflow: hidden;
  }
  .floral-art {
    position: absolute;
    left: 0;
    top: 0;
    width: 760px;
    height: 1040px;
  }
  .brand-name {
    position: absolute;
    left: 62px;
    top: 150px;
    font-family: "Allura", cursive;
    font-weight: 400;
    font-size: 122px;
    line-height: 1;
    color: var(--ink);
    white-space: nowrap;
    transform: rotate(-3deg);
    transform-origin: left center;
  }
  .varietal {
    position: absolute;
    left: 176px;
    top: 850px;
    font-family: "Montserrat", sans-serif;
    font-weight: 400;
    font-size: 46px;
    line-height: 1;
    color: var(--ink);
    white-space: nowrap;
  }
  .vintage {
    position: absolute;
    left: 178px;
    top: 920px;
    font-family: "Montserrat", sans-serif;
    font-weight: 400;
    font-size: 26px;
    line-height: 1;
    letter-spacing: 0.75em;
    color: var(--ink);
    white-space: nowrap;
  }
</style>
</head>
<body>
  <main class="canvas">
    <section class="wine-label">
      <svg class="floral-art" role="img" aria-label="Watercolour illustration of a large peach-pink daisy with a deep red centre, dark stems and a soft pink paint splash" viewBox="0 0 760 1040">
        <defs>
          <radialGradient id="flowerWash" cx="150" cy="505" r="560" gradientUnits="userSpaceOnUse">
            <stop offset="0" stop-color="var(--flower-core)"/>
            <stop offset="0.14" stop-color="var(--petal-deep)"/>
            <stop offset="0.45" stop-color="var(--petal-mid)" stop-opacity="0.75"/>
            <stop offset="0.8" stop-color="var(--petal-light)" stop-opacity="0.5"/>
            <stop offset="1" stop-color="var(--petal-light)" stop-opacity="0"/>
          </radialGradient>
          <radialGradient id="splashWash" cx="720" cy="80" r="120" gradientUnits="userSpaceOnUse">
            <stop offset="0" stop-color="var(--splash)" stop-opacity="0.8"/>
            <stop offset="1" stop-color="var(--splash)" stop-opacity="0"/>
          </radialGradient>
        </defs>
        <ellipse cx="150" cy="505" rx="560" ry="470" fill="url(#flowerWash)"/>
        <ellipse cx="720" cy="80" rx="120" ry="90" fill="url(#splashWash)"/>
      </svg>
      <h1 class="brand-name">Marabel Faye</h1>
      <p class="varietal">PINOT NOIR</p>
      <p class="vintage">2019</p>
    </section>
  </main>
</body>
</html>
```